Hadley & Partners, LLC Business Card 2016

We need a new business card design for a very important trade show coming up.

We are a compliance Consulting Firm. Our clients are stock brokerage firms and investment advisers.

I would like our logo on both sides of the card.

Info in the front of the card shold include:

Logo
First & Last Name
Title
Office #
Cell #
Email
Company Address (42 W. Calloway St., Suite 300 Pasadena, CA 91417

Back of the card should include the logo and url: www.hadleypartnersgroup.com

Target Market(s)

Stock Brokerage Firms and Investment Advisers

Industry/Entity Type

Financial Service

Contact Information for Business Card

Marcus J. Pellew
President
42 W. Calloway St., Suite 300
Pasadena, CA 91417
O 626.555.0147 ext. 204
C 818.555.0193
Email: marcus@hadleypartnersgroup.com
www.hadleypartnersgroup.com

Requirements
Nice to have
• The back of the card could be black with the logo with the white letters.
• I do want the front of the card to at least have the color logo with the black "Hadley & Partners Lettering.

```html
<!DOCTYPE html>
<html lang="en">
<head>
<meta charset="utf-8">
<title>Hadley &amp; Partners — Business Card</title>
<link rel="stylesheet" href="https://fonts.googleapis.com/css2?family=Cinzel:wght@400;600&family=PT+Sans:wght@400;700&display=swap">
<style>
  :root {
    --backdrop: #e6e1d8;
    --card-dark: #000000;
    --card-light: #ffffff;
    --ink: #111111;
    --ink-soft: #333333;
    --on-dark: #ffffff;
    --brand-mark: #c0391f;
    --brand-green: #0f9a4a;
  }
  * { margin: 0; padding: 0; box-sizing: border-box; }
  html, body { width: 960px; height: 1200px; overflow: hidden; }
  body { background: var(--backdrop); position: relative; font-family: "PT Sans", sans-serif; }

  .card { position: absolute; width: 850px; box-shadow: 0 2px 6px rgba(0,0,0,.25); }
  .card--back { left: 55px; top: 86px; height: 487px; background: var(--card-dark); }
  .card--front { left: 55px; top: 628px; height: 484px; background: var(--card-light); }

  .wordmark { position: absolute; display: flex; align-items: center; font-family: "Cinzel", serif; font-weight: 600; white-space: nowrap; }
  .wordmark__square { display: block; background: var(--brand-mark); }
  .card--back .wordmark { left: 0; right: 0; top: 198px; justify-content: center; gap: 22px; color: var(--on-dark); font-size: 44px; }
  .card--back .wordmark__square { width: 56px; height: 56px; }
  .card--front .wordmark { right: 38px; top: 62px; gap: 14px; color: var(--ink); font-size: 30px; }
  .card--front .wordmark__square { width: 38px; height: 38px; }

  .url { position: absolute; left: 0; right: 0; top: 428px; text-align: center; color: var(--on-dark); font-size: 20px; letter-spacing: 4px; }

  .person__name { position: absolute; left: 34px; top: 207px; font-family: "Cinzel", serif; font-weight: 600; font-size: 28px; letter-spacing: 1px; color: var(--ink); }
  .person__title { position: absolute; left: 34px; top: 250px; font-family: "Cinzel", serif; font-size: 19px; letter-spacing: 1px; color: var(--ink-soft); }
  .rule { position: absolute; left: 171px; top: 260px; width: 648px; height: 3px; background: var(--ink); }

  .address { position: absolute; left: 36px; top: 325px; font-size: 21px; line-height: 29px; color: var(--ink); }
  .address__company { color: var(--brand-green); font-weight: 700; font-size: 22px; margin-bottom: 2px; }

  .contact { position: absolute; left: 473px; top: 315px; font-size: 21px; line-height: 35px; color: var(--ink); list-style: none; }
  .contact li { display: flex; align-items: center; gap: 8px; }
  .contact svg { width: 18px; height: 18px; flex: none; }
  .contact__email { padding-left: 2px; }
</style>
</head>
<body>

<section class="card card--back" aria-label="Card back">
  <div class="wordmark"><span class="wordmark__square"></span>HADLEY &amp; PARTNERS</div>
  <p class="url">www.hadleypartnersgroup.com</p>
</section>

<section class="card card--front" aria-label="Card front">
  <div class="wordmark"><span class="wordmark__square"></span>HADLEY &amp; PARTNERS</div>

  <h1 class="person__name">MARCUS J. PELLEW</h1>
  <p class="person__title">PRESIDENT</p>
  <div class="rule"></div>

  <address class="address" style="font-style:normal">
    <div class="address__company">Hadley &amp; Partners, LLC</div>
    <div>42 W. Calloway St., Suite 300</div>
    <div>Pasadena, CA 91417</div>
  </address>

  <ul class="contact">
    <li>
      <svg viewBox="0 0 20 20" aria-label="Office"><path d="M2 7c0-2 3-4 8-4s8 2 8 4v2h-4V7.5c-1-.7-7-.7-8 0V9H2z" fill="#111"/><path d="M5 10h10l2 7H3z" fill="#111"/><circle cx="10" cy="13.5" r="1.8" fill="#fff"/></svg>
      626.555.0147 ext. 204
    </li>
    <li>
      <svg viewBox="0 0 20 20" aria-label="Mobile"><rect x="6" y="3" width="8" height="14" rx="1" fill="none" stroke="#111" stroke-width="1.5"/></svg>
      818.555.0193
    </li>
    <li class="contact__email">marcus@hadleypartnersgroup.com</li>
  </ul>
</section>

</body>
</html>
```